Fern & Hum Holistic Body Oil, logo and label for glas bottles

I need a logo and label design for a new product that will be sold in The Netherlands first, but internationally in the future. The product is a cosmetic Argan oil combined with essential oils. There will be 4 different oils: 1. pure Argan oil, 2. Argan oil with a essential oil blend for Vata, 3. Argan oil with an essential oil blend for Pita, 4. Argan oil with an essential oil blend for Kapha.
The argan oil is 100% biological and handmade from Morocco. The essential oil blends are created by an Ayurvedic practitioner and made in Bali. The different blends Vata, Pita and Kapha refer to the different bodytypes according to Ayurveda.

Each blend will get it's own name, but they are undecided yet, so for now we can call them Vata blend, etc. or follow the names in the document in the attachment, as long as it can be adjusted later on in the design.

We need a label for the front and the back of the bottle. The bottles will be 100 or 150 ml. The label on the front needs to have the logo and brand name on it, the title of the blend and that the oil is 100% bio.
The backside will have a description of the blend (see text in attachment 'benefits' and 'blend' and instructions on how to use it (please create temporary fake text of approx. 3 lines), the website (www.fernandhum.example) and the eco certificate.

The design needs to be natural and clean. Some reference to Morocco and/or Asia is optional. It is a healthcare product. In the attachment I have added some examples of clean designs, they are just meant as inspiration, not as a fixed indication of how the design needs to be.
I WOULD LOVE TO SEE SOME DESIGNS FOR A TRANSPARANT LABEL. THE BOTTLE WILL BE TRANSPARANT GLASS< THE OIL IS A GOLDEN YELLOW COLOR.

Target Market(s)

men and women, but mostly women, age 25-50 years old, interested in healthy living, yoga, biological product, natural products, living a trendy lifestyle, having a good budget for wellness products.

Industry/Entity Type

Health And Wellness

Logo Text

Fern & Hum

Font styles to use
Serif
Decorative
Script

Requirements
Must have
• A design that is easy to adjust if there is a change in the product name. I need to be able to change the text without the available space. A connection to a healthy lifestyle, yoga, wellness, natural lifestyle. And a modern, trendy look.
Nice to have
• unique or playful ways to share the information on the bottle with graphics.
Should not have
• too much decoration and patterns, too many colors combined.

```html
<!DOCTYPE html>
<html lang="en">
<head>
<meta charset="utf-8">
<title>Fern &amp; Hum – Kapha and Vata oil labels</title>
<link rel="stylesheet" href="https://fonts.googleapis.com/css2?family=Playfair+Display:ital,wght@0,400;0,700;0,900;1,400;1,700&family=Libre+Baskerville:ital,wght@0,400;0,700;1,400&display=swap">
<style>
  :root {
    --kapha-blue: #a9d3f2;
    --kapha-blue-light: #c4e2f8;
    --vata-orange: #f8c877;
    --vata-orange-light: #fbdca6;
    --ink: #111111;
    --paper: #ffffff;
    --canvas: #ffffff;
  }
  * { box-sizing: border-box; margin: 0; padding: 0; }
  html, body { width: 849px; height: 1200px; overflow: hidden; background: var(--canvas); }
  .sheet { position: relative; width: 849px; height: 1200px; }

  .label { position: absolute; width: 376px; height: 540px; overflow: hidden; }
  .label--front-kapha { left: 34px; top: 28px; }
  .label--front-vata  { left: 444px; top: 28px; }
  .label--back-kapha  { left: 34px; top: 604px; }
  .label--back-vata   { left: 444px; top: 604px; }

  .label--kapha { background: var(--kapha-blue); }
  .label--vata  { background: var(--vata-orange); }

  .label__glow { position: absolute; left: 0; top: 0; width: 100%; height: 72%; }
  .label--kapha .label__glow { background: radial-gradient(circle at 50% 38%, var(--kapha-blue-light) 0%, rgba(196,226,248,0) 62%); }
  .label--vata .label__glow  { background: radial-gradient(circle at 50% 38%, var(--vata-orange-light) 0%, rgba(251,220,166,0) 62%); }

  .brand-name {
    position: absolute; left: 0; right: 0; top: 62px;
    text-align: center;
    font-family: "Playfair Display", serif;
    font-weight: 700;
    font-size: 88px;
    line-height: 0.9;
    letter-spacing: -1px;
    color: var(--ink);
  }
  .front-info {
    position: absolute; left: 0; right: 0; top: 382px;
    text-align: center; color: var(--paper);
    font-family: "Playfair Display", serif;
  }
  .front-info__bio { font-size: 30px; font-weight: 400; line-height: 1.1; }
  .front-info__oil { font-size: 30px; font-weight: 400; letter-spacing: 1px; text-transform: uppercase; line-height: 1.15; }

  .back-head {
    position: absolute; left: 0; right: 0; top: 26px;
    text-align: center;
    font-family: "Playfair Display", serif;
    font-style: italic; font-weight: 400;
  }
  .back-head__title { font-size: 28px; font-weight: 400; color: var(--ink); line-height: 1.1; }
  .back-head__subtitle { font-size: 27px; color: var(--paper); line-height: 1.15; }

  .back-body {
    position: absolute; left: 24px; right: 24px; top: 112px; bottom: 18px;
    font-family: "Libre Baskerville", serif;
    font-size: 9.5px; line-height: 1.42; color: var(--ink);
  }
  .back-body__heading {
    font-family: "Playfair Display", serif;
    font-style: italic; font-weight: 400;
    font-size: 14px; color: var(--paper);
    margin-bottom: 5px;
  }
  .back-body p { margin-bottom: 9px; }
  .back-body .center { text-align: center; }
  .back-body .dosha { text-align: center; font-size: 11px; }
  .back-body .note { text-align: center; }
</style>
</head>
<body>
<main class="sheet">

  <section class="label label--front-kapha label--kapha">
    <div class="label__glow" role="img" aria-label="Soft circular glow behind the brand name"></div>
    <h1 class="brand-name">Fern<br>&amp;<br>Hum</h1>
    <div class="front-info">
      <p class="front-info__bio">100% Bio</p>
      <p class="front-info__oil">Kapha Oil</p>
    </div>
  </section>

  <section class="label label--front-vata label--vata">
    <div class="label__glow" role="img" aria-label="Soft circular glow behind the brand name"></div>
    <h1 class="brand-name">Fern<br>&amp;<br>Hum</h1>
    <div class="front-info">
      <p class="front-info__bio">100% Bio</p>
      <p class="front-info__oil">Vata Oil</p>
    </div>
  </section>

  <section class="label label--back-kapha label--kapha">
    <header class="back-head">
      <h2 class="back-head__title">Bright Renewal</h2>
      <p class="back-head__subtitle">Kapha Balancing</p>
    </header>
    <div class="back-body">
      <h3 class="back-body__heading">Benefits</h3>
      <p>This blend focuses on the lungs and lymphatic system. Warming oils move heavy energy, lift a dull mood and bring clarity to the chest. Its crisp scent opens the breath and invites a lighter, more active start to each day.</p>
      <p class="center">basil, bergamot, cypress,<br>ginger, juniper, rosemary</p>
      <p class="dosha">+ V, − K</p>
      <p class="center">heating, drying, light</p>
      <p>Stimulates circulation, clears congestion and supports easy digestion. Helps the body release excess fluid and gives the skin a fresh, toned and healthy glow after daily use.</p>
      <p>Warm two or three drops in the palms and massage into the skin with brisk upward strokes, moving toward the heart. Use in the morning after a warm shower.</p>
      <p>For a deeper ritual, add five drops to a warm bath and rest for ten minutes while breathing slowly.</p>
      <p class="note">For external use only. Avoid eyes. Store cool and dark. Patch test first.</p>
    </div>
  </section>

  <section class="label label--back-vata label--vata">
    <header class="back-head">
      <h2 class="back-head__title">Rooted Stillness</h2>
      <p class="back-head__subtitle">Vata Balancing</p>
    </header>
    <div class="back-body">
      <h3 class="back-body__heading">Benefits</h3>
      <p>This blend focuses on the nervous system and the skin. Grounding oils calm a restless mind, soothe dry skin and bring warmth to cold hands and feet. Its soft, sweet scent settles the breath and invites deep rest at night.</p>
      <p class="center">lavender, sandalwood, vetiver,<br>orange, cedarwood, rose</p>
      <p class="dosha">− V, + K</p>
      <p class="center">warming, moist, heavy</p>
      <p>Nourishes dry skin, eases tension in the joints and steadies a busy mind. Helps the body slow down and gives the skin a soft, supple and comforted feel after daily use.</p>
      <p>Warm two or three drops in the palms and massage into the skin with slow circular strokes, moving toward the heart. Use in the evening before sleep.</p>
      <p>For a deeper ritual, add five drops to a warm bath and rest for ten minutes while breathing slowly.</p>
      <p class="note">For external use only. Avoid eyes. Store cool and dark. Patch test first.</p>
    </div>
  </section>

</main>
</body>
</html>
```